Brochure Design Project

Color brochure with text, graphics, and photos. (I will provide the text). 4 pages of 8 1/2 X 11". This is a brochure about dental implants.
Attached is the text and logo for the brochure.

See new parameters and information on the brochure project.

Included in the brochure is our address: Briar Ridge Dental Care, 418 North Cedar Avenue, Briar Ridge, PA 17943.  717-829-4617.  www.briarridgedentalcare.example.

Martin R. Pike, D.M.D., M.A.G.D., F.I.C.O.I. (Attached is photo for brochure)file://localhost/Users/mrpdmd7/Pictures/iPhoto%20Library/Masters/2003/Office%20Pictures/Dr.%20Pike%202.jpg

Target Market(s)

Adults, primarily senior adults.

Industry/Entity Type

Dental

```html
<!DOCTYPE html>
<html lang="en">
<head>
<meta charset="utf-8">
<title>3 Dangers of Tooth Loss – Briar Ridge Dental Care</title>
<link href="https://fonts.googleapis.com/css2?family=Open+Sans:ital,wght@0,400;0,600;0,700;1,400;1,600;1,700&display=swap" rel="stylesheet">
<style>
  :root {
    --brand-blue: #1d5b9c;
    --deep-blue: #16457a;
    --gold: #e2a23a;
    --halo: #cfe3f1;
    --ink: #3a3a3a;
    --heading-ink: #4a4a4a;
    --teal-dot: #2a8aa0;
    --paper: #ffffff;
    --sky: #bfe0ee;
    --sand: #f2e6d4;
  }
  * { box-sizing: border-box; margin: 0; padding: 0; }
  html, body { width: 1200px; height: 776px; overflow: hidden; background: var(--paper); }
  body { font-family: "Open Sans", Arial, sans-serif; color: var(--ink); }

  .spread { position: relative; width: 1200px; height: 776px; overflow: hidden; }
  .backdrop { position: absolute; inset: 0; }

  .practice-mark {
    position: absolute; left: 40px; top: 28px; width: 140px; height: 72px;
    display: flex; align-items: center; gap: 8px;
  }
  .practice-mark .dot { width: 14px; height: 14px; border-radius: 50%; background: var(--paper); flex: none; }
  .practice-mark .name { color: var(--paper); font-size: 15px; font-weight: 600; line-height: 1.25; letter-spacing: .5px; }

  .title { position: absolute; left: 218px; top: 82px; color: var(--heading-ink); font-weight: 400; }
  .title .line { display: block; font-size: 28px; line-height: 38px; }
  .title .small { font-size: 18px; }
  .title em { font-style: italic; }
  .title .big { font-size: 30px; }

  .banner {
    position: absolute; left: 165px; top: 203px; width: 341px; height: 22px;
    background: var(--brand-blue); color: var(--paper);
    font-size: 14px; letter-spacing: 1.6px; line-height: 22px; padding-left: 58px;
  }

  .danger-photo {
    position: absolute; width: 124px; height: 124px; border-radius: 50%;
    background: var(--halo); display: flex; align-items: center; justify-content: center;
  }
  .danger-photo .fill {
    width: 100px; height: 100px; border-radius: 50%;
    background: radial-gradient(circle at 50% 45%, #efe3cf 0%, #d9a79a 55%, #a8564f 100%);
  }

  .danger { position: absolute; left: 196px; width: 365px; font-size: 8.6px; line-height: 13px; }
  .danger h3 { font-size: 10.5px; font-weight: 700; color: #222; line-height: 13px; }
  .danger .sub { font-size: 10.5px; font-style: italic; line-height: 15px; margin-bottom: 14px; }
  .danger h3, .danger .sub, .danger p { padding-left: 20px; }
  .bullet { display: inline-block; width: 20px; margin-left: -20px; color: var(--teal-dot); letter-spacing: -1px; font-size: 10px; }
  .danger p { margin-bottom: 0; }

  .hero {
    position: absolute; left: 600px; top: 0; width: 600px; height: 460px;
  }

  .doctor-frame {
    position: absolute; left: 648px; top: 54px; width: 104px; height: 138px;
    border: 1px solid var(--brand-blue); padding: 3px; background: var(--paper);
  }
  .doctor-frame .fill { width: 100%; height: 100%; border: 3px solid var(--deep-blue);
    background: linear-gradient(180deg, #4b5c73 0%, #8c7566 45%, #2b2f38 100%); }
  .doctor-name { position: absolute; left: 655px; top: 205px; font-size: 9.5px; line-height: 12px; }
  .doctor-name strong { display: block; font-weight: 700; color: #444; }
  .doctor-name span { font-size: 8px; color: #555; }

  .know-head { position: absolute; left: 650px; top: 250px; font-size: 25px; font-weight: 400; color: #222; }
  .know-head strong { font-weight: 700; }

  .story { position: absolute; left: 646px; font-size: 8.6px; line-height: 13px; padding-left: 20px; }
  .story h4 { font-size: 8.8px; font-style: italic; font-weight: 700; color: #333; }
  .story .lead { font-style: italic; font-weight: 700; font-size: 8.8px; color: #333; }
  .story p + p { margin-top: 2px; }
  .story .pull { padding-left: 36px; font-size: 8.8px; line-height: 17px; color: #222; }
</style>
</head>
<body>
<div class="spread">
  <svg class="backdrop" width="1200" height="776" viewBox="0 0 1200 776" aria-hidden="true">
    <defs>
      <linearGradient id="blueField" x1="0" y1="0" x2="1" y2="0">
        <stop offset="0" stop-color="#1b4f8c"/>
        <stop offset="1" stop-color="#2366a8"/>
      </linearGradient>
    </defs>
    <rect width="1200" height="776" fill="url(#blueField)"/>
    <path d="M190 0 C120 220 110 520 205 776 L1200 776 L1200 0 Z" fill="#e2a23a"/>
    <path d="M225 0 C150 230 145 520 245 776 L1095 776 C1170 640 1185 540 1200 470 L1200 0 Z" fill="#ffffff"/>
    <path d="M1095 776 C1170 640 1185 540 1200 470 L1200 776 Z" fill="#e2a23a"/>
    <path d="M210 40 L215 40 C205 60 198 75 192 95 L187 95 Z" fill="#e9b862" opacity=".6"/>
  </svg>

  <div class="practice-mark">
    <span class="dot"></span>
    <span class="name">Briar Ridge<br>Dental Care</span>
  </div>

  <h1 class="title">
    <span class="line">3 Dangers <span class="small">of</span></span>
    <span class="line big"><em>Tooth Loss</em></span>
    <span class="line"><span class="small">and</span> <em style="font-size:24px">Poor Fitting Dentures</em></span>
  </h1>
  <div class="banner">THAT YOU MUST KNOW ABOUT!</div>

  <div class="danger-photo" style="left:78px;top:258px" role="img" aria-label="Close-up photo of worn front teeth and receding gums"><div class="fill"></div></div>
  <div class="danger-photo" style="left:72px;top:410px" role="img" aria-label="Close-up photo of a gap from missing teeth"><div class="fill"></div></div>
  <div class="danger-photo" style="left:78px;top:560px" role="img" aria-label="Close-up photo of decayed teeth and inflamed gums"><div class="fill"></div></div>

  <section class="danger" style="top:255px">
    <h3><span class="bullet">●●●</span>Danger #1</h3>
    <div class="sub">Bone Loss Makes You Look Older Quicker</div>
    <p>Dental Implants assist you in looking and feeling younger, because they prevent bone loss. By preventing bone loss that would normally occur with the loss of teeth, your facial structure remains normal and intact. The chances of wrinkling and aging before your time is less likely to happen.</p>
    <p>&nbsp;In other words, every day that you continue to wear dentures you are experiencing bone loss, which makes you look much older than you have to.</p>
  </section>

  <section class="danger" style="top:400px">
    <h3><span class="bullet">●●●</span>Danger #2</h3>
    <div class="sub">Dentures Increase Your Risk of Heart Disease and Oral Cancer</div>
    <p>While tooth loss may seem like a small problem compared with other health and fitness issues, it is often the first sign of bigger health problems for many people and can put them at higher risk for heart disease and oral cancer.</p>
    <p>When dentures don't fit properly, or are not removed daily, it can lead to bone disease and oral cancer. The National Oral Health Council reports that there will be approximately 30,000 new cases of oral cancer this year alone.</p>
    <p>Heart disease has been linked to gum disease. When dentures do not fit correctly, you have a higher chance of oral problems. You must be aware of these concerns because dentures can cause more problems than just discomfort and a poor smile.</p>
  </section>

  <section class="danger" style="top:591px">
    <h3><span class="bullet">●●●</span>Danger #3</h3>
    <div class="sub">Dentures May Reduce Your Life Span</div>
    <p>It's True! Many people with poor fitting dentures or multiple missing back teeth live up to 10 years less. This is due to poor eating habits and stomach problems. Denture wearers tend to eat more processed foods and experience other health problems related to poor eating habits. People today now have alternatives to dentures, and the best solution is dental implants.</p>
    <p>People who get dental implants can finally eat the healthy foods they have been missing such as; apples, fresh vegetables, corn on the cob, and even steak!</p>
  </section>

  <div class="hero" role="img" aria-label="Photo of a smiling mother and daughter hugging on a sunny beach"
       style="background: radial-gradient(ellipse 60% 70% at 68% 38%, #f0d9bf 0%, #e9cfae 35%, rgba(214,232,240,.85) 62%, rgba(255,255,255,0) 100%), linear-gradient(180deg, rgba(191,224,238,.6) 0%, rgba(255,255,255,0) 100%);
       -webkit-mask-image: linear-gradient(90deg, transparent 0%, #000 22%); mask-image: linear-gradient(90deg, transparent 0%, #000 22%);"></div>

  <div class="doctor-frame" role="img" aria-label="Portrait photo of Dr. Pike"><div class="fill"></div></div>
  <div class="doctor-name"><strong>Martin R. Pike</strong><span>D.M.D., M.A.G.D., F.I.C.O.I.</span></div>

  <h2 class="know-head">Did you <strong>know…</strong></h2>

  <section class="story" style="top:295px;width:290px">
    <p class="lead"><span class="bullet">●●●</span>The quality of your smile has a more direct affect on your life than any other part of your appearance?</p>
    <p style="margin-top:20px">In fact, 88% of all people in North Amercan say they always remember someone with an especially attractive smile. Not only that, 75% agree an unattractive smile can seriously hurt a person's chance for financial success. Perhaps that's why more than half the adults in America wish they could change their smile. Many people want to rid themselves of their frustrating ill-fitting dentures. Some adults want to correct problems they have had since childhood like discolored, crooked or irregularly shaped teeth. Others want to fix conditions they've developed over time, like cracked, worn-</p>
  </section>

  <section class="story" style="top:489px;width:500px">
    <p>down and discolored teeth. There is a good reason for this. You see…</p>
    <h4 style="margin-top:4px"><span class="bullet">●●●</span>Your Smile Can Make Or Break You!</h4>
    <p>For hundreds of years, all the way from Mona Lisa to today's cover girls, a dazzling smile has always carried great significance. It is an indication of a person's sense of well-being and has an enormous impact on a person's health, self-esteem, as well as personal and business relationships. In short…a beautiful smile makes people more attracted to you, and more eager to do business with you.</p>
    <p class="pull" style="margin-top:4px">So, if a smile is so important, why don't more people smile?..and…why don't they smile more often?<br>The answer is simple: Many people are ashamed and embarrassed by their teeth or dentures!</p>
    <h4 style="margin-top:14px"><span class="bullet">●●●</span>Are You A Denture Sufferer?</h4>
    <p>There are many reasons people don't like the appearance of their teeth or dentures: many people are still using old and ill-fitted dentures or partials that pop up, fly out, or get stuck while they are eating or smiling. Some people have teeth too small, to large or crooked. Others have teeth that are gapped or overlapped. Their teeth suffer from stains and discoloration. Some people wear patial or full mouth dentures that don't even fit correctly. Some are crooked, chipped, broken and worn down. And almost everyone wishes their teeth would fit better, be whiter and look more attractive!</p>
    <p>That's the bad news. The good news is every single one of these problems can now be corrected at Briar Ridge Dental Care. Read on to find out how!</p>
  </section>
</div>
</body>
</html>
```